Artwork for single release

I need a cover design for my new single release "Late Neon Waltz" - it's an upbeat jazzy pop number with a slightly dark lyrical edge.

My initial thoughts are that I would like to keep it simple, with just perhaps my name and the name of the track in a bold stylish font and perhaps an image of a female silhouette dancing or walking down a darkened street. However, any other ideas are appreciated.

Please see the track (attached) for reference.

Target Market(s)

16 - 25 alt pop listeners

Requirements
Must have
• Artist name and track name in bold, stylish font:

Rowland Pashby
Late Neon Waltz

Glamorous but somewhat dark feel.

Should not have
• No cliched stock photos or anything too generic.

```html
<!DOCTYPE html>
<html lang="en">
<head>
<meta charset="utf-8">
<title>Rowland Pashby – Late Neon Waltz</title>
<link rel="stylesheet" href="https://fonts.googleapis.com/css2?family=Orbitron:wght@900&display=swap">
<style>
  :root {
    --bg: #000000;
    --bulb-hot: #fff6d8;
    --bulb-mid: #d9c68a;
    --bulb-deep: #8a7440;
    --bulb-rim: #ece6cc;
    --socket: #1e1a10;
  }
  html, body {
    margin: 0;
    padding: 0;
    width: 1200px;
    height: 900px;
    overflow: hidden;
    background: var(--bg);
  }
  .cover {
    position: relative;
    width: 1200px;
    height: 900px;
    background: var(--bg);
  }
  .marquee {
    position: absolute;
    inset: 0;
    width: 1200px;
    height: 900px;
  }
  .marquee__line {
    font-family: "Orbitron", sans-serif;
    font-weight: 900;
    font-size: 170px;
    fill: url(#bulb-grid);
  }
  .bulb-hot { stop-color: var(--bulb-hot); }
  .bulb-mid { stop-color: var(--bulb-mid); }
  .bulb-deep { stop-color: var(--bulb-deep); }
  .bulb-rim { stroke: var(--bulb-rim); }
  .bulb-socket { fill: var(--socket); }
</style>
</head>
<body>
  <main class="cover">
    <svg class="marquee" viewBox="0 0 1200 900" xmlns="http://www.w3.org/2000/svg">
      <defs>
        <radialGradient id="bulb-glow" cx="40%" cy="35%" r="65%">
          <stop offset="0" class="bulb-hot"/>
          <stop offset="0.55" class="bulb-mid"/>
          <stop offset="1" class="bulb-deep"/>
        </radialGradient>
        <pattern id="bulb-grid" patternUnits="userSpaceOnUse" width="10" height="10">
          <rect class="bulb-socket" width="10" height="10"/>
          <circle cx="5" cy="5" r="4.1" fill="url(#bulb-glow)" class="bulb-rim" stroke-width="0.9"/>
        </pattern>
      </defs>
      <text class="marquee__line marquee__line--artist" x="45" y="320"
            textLength="1115" lengthAdjust="spacingAndGlyphs">Rowland Pashby</text>
      <text class="marquee__line marquee__line--title" x="60" y="568"
            textLength="1100" lengthAdjust="spacingAndGlyphs">Late Neon Waltz</text>
    </svg>
  </main>
</body>
</html>
```